Single Side Postcard Size Flyer Design

We want to design an attractive and eye-catching sign for hair stylists and barbers to sit on their workstations to attract the attention of their clients regarding hair loss and encourage them to speak to their stylist about it of they are would like to seek treatment.
Many men and women suffer from hair loss, but are often in denial it is happening or too embarrassed to talk about it.
This postcard sized flyer is designed to stick to the mirror at their hair stylist or barber and encourage them to ask their stylist about it.
We want this to be very plain and simple. With just perhaps some kind of simple head line and worry lines. I have uploaded a simple idea.
I have also uploaded the print templates that must be used to provide final designs.

Target Market(s)

Men aged 25 to 60 with thinning hair

Industry/Entity Type

Healthcare

Font styles to use
Sans Serif

Colors
0355a3
ffffff
cfcfcf
1b1b1b

Requirements
Must have
• Flyer size is vertical 4" x 6"
• Copy for the flyer is as follows ans is in color blue: #014ca5
• Worried About Thinning Hair?
• 2 out of 3 Men will have visible hair loss by age 35.
• The Good News is that your
• Barber or Stylist can tell you how to
• stop the loss & grow back your hair.
• Just ask.
• The Brisk Lattice Program from
• The Marlow Pine Company
• New Science. No Surgery. Your Hair.
• www.quellvantinfo.example
Should not have
• - dont add any logos, images or ornate design. this needs to be simple, easy to ready and eye catching.
• - do not use the color red in any capacity.

```html
<!DOCTYPE html>
<html lang="en">
<head>
<meta charset="utf-8">
<title>Worried About Thinning Hair? – The Marlow Pine Company</title>
<link rel="stylesheet" href="https://fonts.googleapis.com/css2?family=Fira+Sans+Extra+Condensed:wght@500;600&display=swap">
<style>
  :root {
    --ink-blue: #014ca5;
    --band-blue: #0355a3;
    --paper: #ffffff;
    --backdrop: #ffffff;
  }
  * { margin: 0; padding: 0; box-sizing: border-box; }
  html, body {
    width: 1200px; height: 1200px; overflow: hidden;
    background: var(--backdrop);
  }
  .flyer {
    position: absolute;
    left: 246px; top: 73px;
    width: 884px; height: 1316px;
    transform: scale(0.8);
    transform-origin: 0 0;
    background: var(--paper);
    color: var(--ink-blue);
    font-family: "Fira Sans Extra Condensed", "Arial Narrow", sans-serif;
    text-transform: uppercase;
  }
  .frame { position: absolute; left: 0; top: 0; width: 884px; height: 1316px; }
  .line {
    position: absolute; left: 0; width: 884px;
    text-align: center; white-space: nowrap;
  }
  .program-line {
    top: 60px; font-size: 23px; font-weight: 500; line-height: 28px;
    letter-spacing: -0.3px;
  }
  .web-address {
    top: 94px; font-size: 34px; font-weight: 500; line-height: 40px;
    letter-spacing: -0.2px;
  }
  .headline { font-weight: 600; letter-spacing: -0.5px; }
  .headline-top { top: 190px; font-size: 92px; line-height: 100px; }
  .headline-main { top: 278px; font-size: 118px; line-height: 126px; }
  .statistic {
    font-size: 35px; font-weight: 500; line-height: 42px; letter-spacing: -1px;
  }
  .statistic-1 { top: 458px; }
  .statistic-2 { top: 508px; }
  .statistic .figure { font-size: 52px; font-weight: 600; }
  .good-news {
    position: absolute; left: 227px; top: 652px;
    font-size: 35px; font-weight: 500; line-height: 42px; letter-spacing: -1px;
  }
  .ask-band {
    position: absolute; left: 73px; top: 835px;
    width: 741px; height: 171px;
    background: var(--band-blue);
  }
  .ask-text {
    position: absolute; left: 138px; top: 18px;
    color: var(--paper);
    font-size: 112px; font-weight: 600; line-height: 130px;
    letter-spacing: -0.5px;
  }
  .sign-off {
    font-size: 35px; font-weight: 500; line-height: 42px; letter-spacing: -1px;
  }
  .company { top: 1056px; }
  .tagline { top: 1099px; }
</style>
</head>
<body>
  <main class="flyer">
    <svg class="frame" viewBox="0 0 884 1316" aria-hidden="true">
      <g fill="none" stroke="#014ca5" stroke-width="3">
        <polyline points="227,113 71,113 71,509 227,509"/>
        <polyline points="656,113 813,113 813,509 656,509"/>
        <rect x="73" y="603" width="741" height="622"/>
      </g>
    </svg>

    <p class="line program-line">The Brisk Lattice Program from the Marlow Pine</p>
    <p class="line web-address">www.quellvantinfo.example</p>

    <h1 class="line headline headline-top">Worried About</h1>
    <h1 class="line headline headline-main">Thinning Hair?</h1>

    <p class="line statistic statistic-1"><span class="figure">2</span> out of <span class="figure">3</span> men will have</p>
    <p class="line statistic statistic-2">visible hair loss by age 35</p>

    <p class="good-news">The good news is that your barber<br>or stylist can tell you how to stop<br>the loss &amp; grow back your hair.</p>

    <div class="ask-band">
      <p class="ask-text">- Just ask.</p>
    </div>

    <p class="line sign-off company">The Marlow Pine Company</p>
    <p class="line sign-off tagline">New Science. No Surgery. Your Hair.</p>
  </main>
</body>
</html>
```